Modern Yoga Studio Timetable and Flyer Design

We have a comprehensive class timetable and we are wanting to a clean modern look for our Spring timetable.

We require a double sided flyer with our class timetable included.
We would prefer an A5 size (postcard) or DL (1/3 A4).

We would like the final flyer to have.
Side A : Yoga image, logo

Cedar Pose Loft
address: 3/17 Weltmore Street, Parvindale
website: cedarpose.com.au
mobile: 0471 592 640

Side B: Clear easy to read timetable with a break down of class types and website.

We would also like to have a copy of the timetable itself as a separate jpg or pdf for use on our website to download.

Thank you.
Yours kindly,
Hilde

I have attached a sample of another timetable of which I like the look and feel of, however this is just a guide. I've also attached our 'new' schedule in WORD plus uploaded our last design of the front.

Target Market(s)

Women aged 30-45

Industry/Entity Type

Health And Wellness

Font styles to use
Other font styles liked:
• Brandon Grotesque, Jenna Sue

Colors
6c459b
33a6d7
ffffff

Requirements
Must have
• A definitive colour to decipher between different class types on our timetable. Where each colour represents a different class type. Colours and layouts similar to our website design, see www.cedarpose.com.au
Nice to have
• I've included a design of another studio whose timetable design I like. One of our own yoga images instead of a stock image.
Should not have
• No dark gridlines between the cells/boxes in the timetables. Please don't use stock yoga images.

```html
<!DOCTYPE html>
<html lang="en">
<head>
<meta charset="utf-8">
<title>Cedar Pose Loft – Spring Flyer</title>
<link href="https://fonts.googleapis.com/css2?family=Quicksand:wght@400;500;600&family=Montserrat:wght@700;800&family=Fira+Sans+Condensed:wght@400;500&display=swap" rel="stylesheet">
<style>
  :root {
    --purple: #6c459b;
    --purple-deep: #5a3687;
    --blue: #33a6d7;
    --white: #ffffff;
    --page: #ebe8ee;
    --row-blue: #c9e7f6;
    --row-pink: #f3d6ea;
    --cell-purple: #b47ec3;
    --cell-blue: #8fcdf1;
    --ink: #2a2233;
    --frame: #2e2440;
  }
  * { box-sizing: border-box; margin: 0; padding: 0; }
  html, body { width: 1200px; height: 851px; overflow: hidden; }
  body { background: var(--page); position: relative; font-family: "Quicksand", sans-serif; }

  /* ---------- Side A: DL flyer front ---------- */
  .flyer-front {
    position: absolute; left: 79px; top: 123px;
    width: 302px; height: 623px;
    background: var(--white);
    box-shadow: 0 6px 18px rgba(40, 20, 60, .18);
    overflow: hidden;
  }
  .ornament-area {
    position: absolute; left: 50px; top: 0; width: 202px; height: 66px;
    border-radius: 0 0 101px 101px;
    background: radial-gradient(circle at 50% 0%, #6c459b 0%, #9a80c0 40%, #e3dcef 75%, #ffffff 100%);
  }
  .brand-mark {
    position: absolute; left: 0; right: 0; top: 76px;
    text-align: center;
    font-family: "Quicksand", sans-serif; font-weight: 500;
    font-size: 19px; letter-spacing: 3px; color: var(--blue);
  }
  .hero { position: absolute; left: 0; top: 132px; width: 302px; height: 300px; }
  .studio-name {
    position: absolute; left: 0; right: 0; top: 430px;
    text-align: center;
    font-family: "Quicksand", sans-serif; font-weight: 600;
    font-size: 30px; color: var(--purple);
  }
  .contact-box {
    position: absolute; left: 17px; top: 494px; width: 268px; height: 90px;
    border: 3px solid var(--purple); border-bottom: none;
    border-radius: 14px 14px 0 0;
    padding: 8px 8px 0 10px;
  }
  .contact-phone {
    display: flex; align-items: center; gap: 4px;
    font-size: 32px; font-weight: 400; color: var(--purple); line-height: 1.1;
  }
  .contact-phone svg { width: 14px; height: 14px; flex: none; }
  .contact-address {
    display: flex; align-items: center; gap: 6px; margin-top: 4px;
    font-size: 14.5px; font-weight: 500; color: var(--ink); white-space: nowrap;
  }
  .contact-address svg { width: 10px; height: 13px; flex: none; }
  .web-band {
    position: absolute; left: 0; right: 0; bottom: 0; height: 47px;
    background: var(--blue); color: var(--white);
    display: flex; align-items: center; justify-content: center;
    font-size: 19px; font-weight: 500;
  }

  /* ---------- Side B: timetable card ---------- */
  .timetable-card {
    position: absolute; left: 429px; top: 291px;
    width: 696px; height: 339px;
    background: var(--white);
    box-shadow: 0 6px 18px rgba(40, 20, 60, .18);
    padding: 20px 20px 0 17px;
  }
  .timetable-title {
    font-family: "Montserrat", sans-serif; font-weight: 800;
    font-size: 11.5px; color: var(--purple); margin-left: 16px; letter-spacing: .2px;
  }
  .timetable {
    margin-top: 4px;
    border: 2px solid var(--frame); border-radius: 10px; overflow: hidden;
    background: var(--white);
  }
  .timetable table { width: 100%; border-collapse: collapse; table-layout: fixed; }
  .timetable col.time-col { width: 68px; }
  .timetable thead th {
    background: var(--purple); color: var(--white);
    font-family: "Montserrat", sans-serif; font-weight: 700; font-size: 9.5px;
    height: 19px; text-align: center;
  }
  .timetable tbody td {
    height: 19.8px; padding: 0 0 0 10px;
    font-family: "Fira Sans Condensed", sans-serif; font-size: 11px; color: var(--ink);
    border-top: 2px solid var(--white); border-right: 2px solid var(--white);
    white-space: nowrap; text-transform: uppercase;
  }
  .timetable tbody td.time { font-family: "Quicksand", sans-serif; font-weight: 600; font-size: 10.5px; padding-left: 16px; text-transform: uppercase; }
  .timetable tbody tr:nth-child(odd) td { background: var(--row-blue); }
  .timetable tbody tr:nth-child(even) td { background: var(--row-pink); }
  .timetable tbody td.class-purple { background: var(--cell-purple) !important; color: var(--white); }
  .timetable tbody td.class-blue { background: var(--cell-blue) !important; color: var(--ink); }
  .timetable-note { margin: 5px 0 0 12px; font-size: 11.5px; font-weight: 600; color: var(--ink); }
</style>
</head>
<body>

  <section class="flyer-front" aria-label="Flyer front">
    <div class="ornament-area" role="img" aria-label="Purple mandala ornament"></div>
    <div class="brand-mark">Cedar Pose Loft</div>

    <svg class="hero" viewBox="0 0 302 300" aria-hidden="false">
      <defs>
        <clipPath id="hero-shape">
          <path d="M0 52 Q150 40 302 8 L302 226 Q200 236 160 268 L151 282 L142 268 Q100 236 0 226 Z"/>
        </clipPath>
        <linearGradient id="hero-tones" x1="0" y1="0" x2="0" y2="1">
          <stop offset="0" stop-color="#f4f1f2"/>
          <stop offset=".55" stop-color="#d9cfd4"/>
          <stop offset=".7" stop-color="#a88a66"/>
          <stop offset="1" stop-color="#8a6c4a"/>
        </linearGradient>
      </defs>
      <g role="img" aria-label="Photo of a woman holding a side angle yoga pose on a mat">
        <rect width="302" height="300" fill="url(#hero-tones)" clip-path="url(#hero-shape)"/>
      </g>
      <path d="M0 52 Q150 40 302 8 L302 20 Q160 52 0 64 Z" fill="var(--purple)"/>
      <path d="M200 34 Q260 18 302 0 L302 10 Q250 28 200 34 Z" fill="var(--blue)"/>
      <path d="M0 222 Q100 232 142 264 L151 280 L160 264 Q200 232 302 222 L302 230 Q204 240 164 270 L151 292 L138 270 Q98 240 0 230 Z" fill="var(--blue)"/>
    </svg>

    <div class="studio-name">Cedar Pose Loft</div>

    <div class="contact-box">
      <div class="contact-phone">
        <svg viewBox="0 0 24 24"><path d="M6.6 10.8a15.1 15.1 0 0 0 6.6 6.6l2.2-2.2a1 1 0 0 1 1-.25 11.4 11.4 0 0 0 3.6.57 1 1 0 0 1 1 1V20a1 1 0 0 1-1 1A17 17 0 0 1 3 4a1 1 0 0 1 1-1h3.5a1 1 0 0 1 1 1c0 1.25.2 2.45.57 3.57a1 1 0 0 1-.25 1z" fill="var(--purple)"/></svg>
        <span>0471 592 640</span>
      </div>
      <div class="contact-address">
        <svg viewBox="0 0 10 14"><path d="M5 0a5 5 0 0 0-5 5c0 3.8 5 9 5 9s5-5.2 5-9a5 5 0 0 0-5-5zm0 7a2 2 0 1 1 0-4 2 2 0 0 1 0 4z" fill="var(--purple)"/></svg>
        <span>3/17 Weltmore Street, Parvindale</span>
      </div>
    </div>
    <div class="web-band">website: cedarpose.com.au</div>
  </section>

  <section class="timetable-card" aria-label="Flyer back">
    <h1 class="timetable-title">CEDAR POSE SPRING TIMETABLE</h1>
    <div class="timetable">
      <table>
        <colgroup><col class="time-col"><col><col><col><col><col><col><col></colgroup>
        <thead>
          <tr><th></th><th>MON</th><th>TUE</th><th>WED</th><th>THU</th><th>FRI</th><th>SAT</th><th>SUN</th></tr>
        </thead>
        <tbody>
          <tr><td class="time">545am</td><td></td><td class="class-blue">Rise + Shine*</td><td></td><td class="class-blue">Rise + Shine*</td><td></td><td></td><td></td></tr>
          <tr><td class="time">900am</td><td></td><td></td><td></td><td></td><td></td><td class="class-purple">Vinyasa Flow</td><td></td></tr>
          <tr><td class="time">915am</td><td></td><td class="class-blue">Vinyasa Flow</td><td></td><td></td><td></td><td></td><td class="class-blue">Yin</td></tr>
          <tr><td class="time">930am</td><td class="class-purple">Slow Flow</td><td></td><td></td><td class="class-purple">Vinyasa Flow</td><td></td><td></td><td></td></tr>
          <tr><td class="time">1030am</td><td></td><td></td><td></td><td></td><td></td><td class="class-blue">Pregnancy*</td><td></td></tr>
          <tr><td class="time">11am</td><td></td><td class="class-purple">Mum + Baby*</td><td></td><td class="class-purple">Mum + Baby*</td><td></td><td></td><td></td></tr>
          <tr><td class="time">1215pm</td><td></td><td></td><td></td><td class="class-blue">Pregnancy</td><td></td><td></td><td></td></tr>
          <tr><td class="time">4pm</td><td></td><td></td><td class="class-purple">Kids 8-12*</td><td class="class-purple">Kids 5-7*</td><td></td><td class="class-purple">Vinyasa Flow</td><td></td></tr>
          <tr><td class="time">445pm</td><td></td><td></td><td class="class-blue">Teens 12-16*</td><td></td><td></td><td></td><td></td></tr>
          <tr><td class="time">500pm</td><td></td><td></td><td></td><td class="class-purple">Teens 12 – 16*</td><td></td><td></td><td></td></tr>
          <tr><td class="time">600pm</td><td class="class-blue">Pregnancy*</td><td class="class-blue">Vinyasa Flow</td><td class="class-blue">Slow Flow</td><td></td><td class="class-blue">Flow + Restore</td><td></td><td></td></tr>
          <tr><td class="time">615pm</td><td></td><td></td><td></td><td class="class-purple">Pregnancy*</td><td></td><td></td><td></td></tr>
          <tr><td class="time">730pm</td><td class="class-blue">Vinyasa Flow</td><td class="class-blue">Pregnancy*</td><td class="class-blue">Yin + Restore</td><td class="class-blue">Women's Wellness*</td><td></td><td></td><td></td></tr>
        </tbody>
      </table>
    </div>
    <p class="timetable-note">* bookings essential</p>
  </section>

</body>
</html>
```